Poster design for a vet clinic

Running a campaign called 'Pal Spotter', which is where people get a $30 voucher for themselves and their friend if they refer somebody to our vet clinic.

Text something like:
We love Pal Spotters!
Refer a fur friend to our friendly team and both your fur child and their fur child will receive a $30 voucher to use in clinic! *
* Limited to one pet per fur parent and the referred fur parent must be new to our clinic. Unlimited vouchers for number of referrals!

I want it to be cute but professional. You can see the design styles at vettoly.com.au/northryde and see the logo there too.
I am thinking of having a dog whispering to a cat or something like that as the main image.
I would like both the photoshop file and the pdf please. Would be for an A2 poster.

```html
<!DOCTYPE html>
<html lang="en">
<head>
<meta charset="UTF-8">
<title>We Love Pal Spotters – Referral Poster</title>
<link rel="stylesheet" href="https://fonts.googleapis.com/css2?family=Anton&family=Oswald:wght@600&display=swap">
<style>
  :root {
    --paper: #fbfaf8;
    --paw-tint: #ece6df;
    --orange: #f7941d;
    --tan: #e0aa5c;
    --maroon: #74313f;
    --rule: #111111;
  }
  * { margin: 0; padding: 0; box-sizing: border-box; }
  html, body { width: 847px; height: 1200px; overflow: hidden; background: var(--paper); }
  .poster {
    position: relative;
    width: 847px;
    height: 1200px;
    background: radial-gradient(ellipse at 50% 60%, var(--paper) 0%, var(--paper) 55%, var(--paw-tint) 140%);
    overflow: hidden;
  }
  .hero-art {
    position: absolute;
    left: 8px;
    top: 0;
    width: 815px;
    height: 440px;
    border-radius: 0 0 200px 200px;
    background: linear-gradient(100deg, var(--orange) 0%, var(--orange) 45%, var(--tan) 60%, var(--maroon) 100%);
  }
  .headline {
    position: absolute;
    left: 0;
    width: 100%;
    text-align: center;
    font-family: "Anton", "Oswald", sans-serif;
    text-transform: uppercase;
    line-height: 1;
  }
  .headline--love {
    top: 448px;
    font-size: 136px;
    color: var(--orange);
    letter-spacing: 0.28em;
    padding-left: 0.28em;
  }
  .headline--love .dot {
    display: inline-block;
    width: 26px;
    height: 26px;
    border-radius: 50%;
    background: var(--orange);
    vertical-align: middle;
    margin: 0 12px 0 0;
    position: relative;
    top: -10px;
  }
  .headline--love .dot--end { margin: 0 0 0 -26px; }
  .headline--pal {
    top: 578px;
    font-size: 136px;
    color: var(--maroon);
    letter-spacing: 0.3em;
    padding-left: 0.3em;
  }
  .headline--spotters {
    top: 712px;
    font-size: 150px;
    color: var(--maroon);
    letter-spacing: 0.04em;
  }
  .offer, .terms {
    position: absolute;
    left: 30px;
    right: 30px;
    text-align: center;
    font-family: "Oswald", "Anton", sans-serif;
    font-weight: 600;
    text-transform: uppercase;
    font-size: 27px;
    line-height: 1.28;
  }
  .offer { top: 886px; color: var(--orange); }
  .divider {
    position: absolute;
    left: 45px;
    top: 1018px;
    width: 770px;
    height: 14px;
    border-radius: 7px;
    background: var(--rule);
  }
  .terms { top: 1062px; color: var(--maroon); }
</style>
</head>
<body>
  <main class="poster">
    <div class="hero-art" role="img" aria-label="Illustration of a smiling orange cat and a happy tan dog whispering cheek to cheek"></div>

    <h1>
      <span class="headline headline--love"><span class="dot"></span>We Love<span class="dot dot--end"></span></span>
      <span class="headline headline--pal">Pal</span>
      <span class="headline headline--spotters">Spotters!</span>
    </h1>

    <p class="offer">
      Refer a fur friend to our friendly team and both your fur<br>
      child and their fur child will receive a 30 $<br>
      voucher to use in clinic!
    </p>

    <div class="divider"></div>

    <p class="terms">
      Limited to one pet per fur parent and<br>
      the referred fur parent must be new to our clinic.<br>
      Unlimited vouchers for number of referrals!
    </p>
  </main>
</body>
</html>
```